" Cavalto Solutions oferece serviços de automação de tarefas manuais repetitivas realizadas na administração das empresas, como ingresso de faturas, coleta de dados de vários sistemas e consolidação manual, aceso a site para extração de dados e posterior registro em sistemas próprios, etc. Os serviços que oferece são: a identificação dessas oportunidades apoiando no budiness case, o desenvolvimento dos robôs para automação, a implantação do modelo de governança para assegurar a boa implantação e posterior sustentabilidade, transferência de conhecimento para as equipes internos, e finalmente o suporte e manutenção da plataforma. "

```html
<!DOCTYPE html>
<html lang="pt-BR">
<head>
<meta charset="UTF-8">
<title>Cavalto Solutions — Quem Somos</title>
<link href="https://fonts.googleapis.com/css2?family=Open+Sans:wght@300;400;600;700&display=swap" rel="stylesheet">
<style>
  :root {
    --teal: #3bb3cf;
    --teal-dark: #2a8fb0;
    --navy: #1f3550;
    --text: #555b61;
    --muted: #9aa1a7;
    --band: #f1f2f3;
    --card: #f6f7f8;
    --white: #ffffff;
    --line: #e3e5e7;
  }
  * { box-sizing: border-box; margin: 0; padding: 0; }
  html, body { width: 1200px; height: 1200px; overflow: hidden; }
  body {
    background: var(--white);
    font-family: "Open Sans", Arial, sans-serif;
    color: var(--text);
  }
  .topbar {
    height: 44px;
    background: var(--teal);
    display: flex;
    justify-content: flex-end;
    align-items: center;
    padding: 0 80px;
    color: var(--white);
    font-size: 15px;
    gap: 8px;
  }
  .header {
    height: 120px;
    display: flex;
    align-items: center;
    justify-content: space-between;
    padding: 0 80px;
    border-bottom: 1px solid var(--line);
  }
  .brand { display: flex; align-items: center; gap: 14px; }
  .brand-mark { width: 34px; height: 34px; background: var(--teal); }
  .brand-name { font-size: 30px; font-weight: 600; color: var(--navy); }
  .nav { display: flex; gap: 38px; font-size: 17px; font-weight: 600; color: var(--navy); }
  .nav .active { color: var(--teal); }
  .page-band {
    height: 120px;
    background: var(--band);
    padding: 28px 80px;
  }
  .page-title { font-size: 30px; font-weight: 600; color: var(--navy); }
  .breadcrumb { font-size: 14px; color: var(--muted); margin-top: 4px; }
  .about {
    display: flex;
    gap: 50px;
    padding: 60px 80px;
  }
  .about-photo {
    width: 540px;
    height: 390px;
    flex-shrink: 0;
    background: linear-gradient(135deg, #8fc6d9 0%, #4f8fae 45%, #2b4a63 100%);
  }
  .about-text { padding-top: 6px; }
  .about-text h2 {
    font-size: 36px;
    font-weight: 400;
    color: var(--navy);
    margin-bottom: 22px;
  }
  .about-text p { font-size: 19px; line-height: 1.75; }
  .values {
    display: flex;
    gap: 30px;
    padding: 0 80px;
  }
  .value-card {
    flex: 1;
    height: 290px;
    background: var(--card);
    border-top: 1px solid var(--line);
    display: flex;
    flex-direction: column;
    align-items: center;
    justify-content: center;
    gap: 26px;
  }
  .value-card h3 {
    font-size: 30px;
    font-weight: 400;
    color: var(--teal);
  }
  .value-icon {
    width: 140px;
    height: 140px;
    border-radius: 50%;
    background: linear-gradient(135deg, #6fb7d3, #2a5f86);
  }
</style>
</head>
<body>
  <div class="topbar">
    <svg width="16" height="16" viewBox="0 0 24 24" aria-hidden="true"><path fill="#fff" d="M6.6 10.8a15.1 15.1 0 0 0 6.6 6.6l2.2-2.2c.3-.3.7-.4 1-.2 1.1.4 2.3.6 3.6.6.6 0 1 .4 1 1V20c0 .6-.4 1-1 1C10.6 21 3 13.4 3 4c0-.6.4-1 1-1h3.5c.6 0 1 .4 1 1 0 1.3.2 2.5.6 3.6.1.3 0 .7-.2 1z"/></svg>
    <span>(11) 4002-3100</span>
  </div>
  <header class="header">
    <div class="brand">
      <span class="brand-mark"></span>
      <span class="brand-name">Cavalto Solutions</span>
    </div>
    <nav class="nav">
      <span class="active">Home</span>
      <span>Quem Somos</span>
      <span>RPA</span>
      <span>Serviços ▾</span>
      <span>Contato</span>
    </nav>
  </header>
  <section class="page-band">
    <h1 class="page-title">Quem Somos</h1>
    <div class="breadcrumb">Home / Quem Somos</div>
  </section>
  <section class="about">
    <div class="about-photo" role="img" aria-label="Foto de executivo tocando interface digital de automação"></div>
    <div class="about-text">
      <h2>QUEM SOMOS</h2>
      <p>Oferecemos nossos serviços de automação com RPA Robotic Process Automation, uma tecnologia para otimizar a automatizar de serviços e aplicativos os benefícios desta solução, gerando economia para a companhia.</p>
    </div>
  </section>
  <section class="values">
    <div class="value-card">
      <h3>MISSÃO</h3>
      <div class="value-icon" role="img" aria-label="Imagem ilustrativa da missão"></div>
    </div>
    <div class="value-card">
      <h3>VISÃO</h3>
      <div class="value-icon" role="img" aria-label="Imagem ilustrativa da visão"></div>
    </div>
    <div class="value-card">
      <h3>VALORES</h3>
      <div class="value-icon" role="img" aria-label="Imagem ilustrativa dos valores"></div>
    </div>
  </section>
</body>
</html>
```